Banner Ad Design Project

I just launched an affiliate program for my company (Brisk Academy), and I need some web ads and banners created. 6 in total.Here are the specs for the ads:
W120XH90- Small Web Ad
W120XH160- Big Web Ad
W468XH60- Full Banner Ad
W250XH250- Big Banner Ad
W125XH125- Samll Square Ad
W160XH600- Wide Skyscraper
I've uploaded one example I made hower I am looking for a more professional look. You'll also see a few flyers I've uploaded. These will get you an idea of the product.
Here is what I am looking to achieve and a little background on my product:
BRISK Academy’s first course, ‘Ready on Shift’ is a 30 minute interactive training and certification course specifically designed for teens and young adults to better prepare them for the workplace. The training is based on employer feedback, delivered on a peer-to-peer level, industry nonspecific, mobile ready and covers the following challenges:
• Work Ethic
• Social Media
• Cell Phone Issues
• Communication and Manners Matter
• Hygiene and more.
These ads are to catch the eyes of bosses, supervisors and managers. Basically anyone who is looking to improve workplace performance. Our website is www.briskacademy.example. Please look it over for our branding. Thanks so much!
ps- Please make 1/2 static banners and 1/2 animated (gif of flash) banner.
Target Market(s)
Bosses, supervisors and managers. Anyone who employees teenagers and young adults and is looking to train them to better serve their customers.
Industry/Entity Type
Training
Look and feel

```html
<!DOCTYPE html>
<html lang="en">
<head>
<meta charset="utf-8">
<title>Brisk Academy – Banner Set</title>
<link rel="stylesheet" href="https://fonts.googleapis.com/css2?family=Oswald:wght@400;500;700&display=swap">
<style>
  :root {
    --board-light: #a9a6a6;
    --board-dark: #7d7b7c;
    --blue-top: #2f8de0;
    --blue-bottom: #0b3b86;
    --red-top: #d91c20;
    --red-bottom: #9c0d10;
    --yellow-top: #fff36a;
    --yellow-bottom: #f2c200;
    --headline-shadow: #1a1a1a;
    --white: #ffffff;
    --ink: #1d1d1d;
    --logo-blue: #1f4fa8;
    --photo-a: #7bb4e6;
    --photo-b: #2a3a55;
  }
  * { box-sizing: border-box; margin: 0; padding: 0; }
  html, body { width: 1200px; height: 1106px; overflow: hidden; }
  body {
    background: linear-gradient(160deg, var(--board-light) 0%, var(--board-dark) 100%);
    font-family: "Oswald", "Arial Narrow", sans-serif;
  }
  .board {
    position: absolute; left: 0; top: 0;
    width: 928px; height: 855px;
    transform: scale(1.2931);
    transform-origin: 0 0;
  }
  .ad { position: absolute; overflow: hidden; color: var(--white); }
  .bg-blue { background: linear-gradient(180deg, var(--blue-top), var(--blue-bottom)); }
  .bg-red { background: linear-gradient(180deg, var(--red-top), var(--red-bottom)); }

  .logo {
    position: absolute; background: var(--white);
    display: flex; align-items: center; justify-content: center; gap: 4px;
    color: var(--logo-blue); font-weight: 700; text-align: center; line-height: 1;
  }
  .logo .mark { border-radius: 50%; background: var(--logo-blue); flex: none; }

  .strip-red { position: absolute; background: linear-gradient(180deg, var(--red-top), var(--red-bottom)); }
  .strip-blue { position: absolute; background: linear-gradient(180deg, var(--blue-top), var(--blue-bottom)); }

  .headline {
    position: absolute; left: 0; right: 0; text-align: center;
    font-weight: 700; line-height: 1; text-transform: uppercase;
    background: linear-gradient(180deg, var(--yellow-top), var(--yellow-bottom));
    -webkit-background-clip: text; background-clip: text; color: transparent;
    filter: drop-shadow(1px 1px 0 var(--headline-shadow));
  }
  .copy { position: absolute; font-weight: 500; line-height: 1.3; text-align: center; }
  .ticks { position: absolute; list-style: none; font-weight: 500; line-height: 1.55; }
  .ticks li::before { content: "\2713\00a0"; }

  .photo { position: absolute; background: linear-gradient(180deg, var(--photo-a), var(--photo-b)); }

  .cta {
    position: absolute; display: flex; align-items: center; justify-content: center; gap: 6px;
    border-radius: 3px; font-weight: 400; white-space: nowrap;
  }
  .cta-red { background: linear-gradient(180deg, var(--red-top), var(--red-bottom)); color: var(--white); box-shadow: 0 1px 2px rgba(0,0,0,.4); }
  .cta-yellow { background: linear-gradient(180deg, var(--yellow-top), var(--yellow-bottom)); color: var(--ink); box-shadow: 0 1px 2px rgba(0,0,0,.4); }
</style>
</head>
<body>
<div class="board">

  <!-- Skyscraper: Teaching Workplace -->
  <section class="ad bg-blue" style="left:97px;top:70px;width:160px;height:600px;">
    <div class="logo" style="left:0;top:0;width:160px;height:143px;font-size:22px;">
      <span class="mark" style="width:12px;height:12px;"></span>Brisk Academy
    </div>
    <div class="strip-red" style="left:0;top:143px;width:160px;height:10px;"></div>
    <h2 class="headline" style="top:163px;font-size:34px;">Teaching</h2>
    <h3 class="headline" style="top:203px;font-size:27px;">Workplace</h3>
    <p class="copy" style="left:4px;right:4px;top:240px;font-size:14px;">skills to teens &amp; young adults, transforming them into valued employees &amp; customer service ambassadors.</p>
    <div class="photo" role="img" aria-label="Photo of smiling young adults holding books" style="left:0;top:372px;width:160px;height:228px;"></div>
    <div class="cta cta-red" style="left:8px;top:555px;width:147px;height:33px;font-size:17px;">Free Preview!
      <svg width="16" height="16" viewBox="0 0 16 16"><circle cx="8" cy="8" r="7" fill="#b00d10" stroke="#ff6a6a" stroke-width="1"/><path d="M5 8h5M8 5.5 10.5 8 8 10.5" stroke="#fff" stroke-width="1.6" fill="none"/></svg>
    </div>
  </section>

  <!-- Skyscraper: Employee Training -->
  <section class="ad bg-red" style="left:284px;top:70px;width:160px;height:600px;">
    <div class="logo" style="left:0;top:0;width:160px;height:143px;font-size:22px;">
      <span class="mark" style="width:12px;height:12px;"></span>Brisk Academy
    </div>
    <div class="strip-blue" style="left:0;top:143px;width:160px;height:10px;"></div>
    <h2 class="headline" style="top:163px;font-size:33px;">Employee</h2>
    <h3 class="headline" style="top:203px;font-size:39px;">Training</h3>
    <ul class="ticks" style="left:7px;top:249px;font-size:13px;">
      <li>Covering Social Media.</li>
      <li>Texting &amp; Cell Phones.</li>
      <li>Grooming &amp; Hygiene.</li>
    </ul>
    <div class="photo" role="img" aria-label="Photo of a smiling businesswoman in a dark suit" style="left:0;top:330px;width:160px;height:270px;background:linear-gradient(180deg,#c41416,#2b2226);"></div>
    <div class="cta cta-yellow" style="left:12px;top:553px;width:133px;height:32px;font-size:17px;">Free Preview!</div>
  </section>

  <!-- 250 x 250 -->
  <section class="ad bg-blue" style="left:501px;top:120px;width:250px;height:250px;">
    <div class="photo" role="img" aria-label="Photo of three young adults standing together" style="left:135px;top:0;width:115px;height:250px;"></div>
    <div class="logo" style="left:0;top:0;width:135px;height:75px;font-size:15px;">
      <span class="mark" style="width:9px;height:9px;"></span>Brisk Academy
    </div>
    <div class="strip-red" style="left:0;top:75px;width:140px;height:7px;"></div>
    <h2 class="headline" style="top:103px;right:auto;left:5px;font-size:33px;">Teaching</h2>
    <h3 class="headline" style="top:143px;right:auto;left:5px;font-size:25px;">Workplace Skills</h3>
    <ul class="ticks" style="left:7px;top:182px;font-size:12px;">
      <li>Covering Social Media.</li>
      <li>Texting &amp; Cell Phones.</li>
      <li>Grooming &amp; Hygiene.</li>
    </ul>
    <div class="cta cta-red" style="left:145px;top:218px;width:100px;height:23px;font-size:12px;">Free Preview!
      <svg width="11" height="11" viewBox="0 0 16 16"><circle cx="8" cy="8" r="7" fill="#b00d10"/><path d="M5 8h5M8 5.5 10.5 8 8 10.5" stroke="#fff" stroke-width="1.8" fill="none"/></svg>
    </div>
  </section>

  <!-- 120 x 160 -->
  <section class="ad bg-blue" style="left:506px;top:406px;width:120px;height:160px;">
    <h2 class="headline" style="top:3px;font-size:22px;">Teaching</h2>
    <h3 class="headline" style="top:29px;font-size:12px;">Workplace Skills</h3>
    <ul class="ticks" style="left:7px;top:46px;font-size:9px;">
      <li>Covering Social Media.</li>
      <li>Texting &amp; Cell Phones.</li>
      <li>Grooming &amp; Hygiene.</li>
    </ul>
    <div class="logo" style="left:0;top:115px;width:120px;height:45px;"></div>
    <div class="photo" role="img" aria-label="Photo of three young adults" style="left:58px;top:95px;width:62px;height:65px;"></div>
    <div class="logo" style="left:0;top:115px;width:56px;height:45px;gap:3px;padding:0 3px;font-size:9px;line-height:1.1;text-align:left;">
      <span class="mark" style="width:5px;height:5px;"></span><span>Brisk<br>Academy</span>
    </div>
    <div class="cta cta-red" style="left:54px;top:139px;width:62px;height:14px;font-size:8px;">Free Preview!</div>
  </section>

  <!-- 125 x 125 -->
  <section class="ad bg-blue" style="left:655px;top:406px;width:125px;height:125px;">
    <div class="photo" role="img" aria-label="Photo of three young adults standing together" style="left:70px;top:0;width:55px;height:125px;"></div>
    <div class="logo" style="left:0;top:0;width:70px;height:36px;font-size:9px;">
      <span class="mark" style="width:5px;height:5px;"></span>Brisk Academy
    </div>
    <div class="strip-red" style="left:0;top:36px;width:72px;height:4px;"></div>
    <h2 class="headline" style="top:51px;right:auto;left:3px;font-size:16px;">Teaching</h2>
    <h3 class="headline" style="top:70px;right:auto;left:3px;font-size:13px;">Workplace Skills</h3>
    <ul class="ticks" style="left:4px;top:89px;font-size:6.5px;line-height:1.5;">
      <li>Covering Social Media.</li>
      <li>Texting &amp; Cell Phones.</li>
      <li>Grooming &amp; Hygiene.</li>
    </ul>
    <div class="cta cta-red" style="left:73px;top:109px;width:48px;height:11px;font-size:6px;">Free Preview!</div>
  </section>

  <!-- 468 x 60 -->
  <section class="ad bg-blue" style="left:90px;top:723px;width:468px;height:60px;">
    <div class="logo" style="left:0;top:0;width:84px;height:60px;font-size:11px;">
      <span class="mark" style="width:6px;height:6px;"></span>Brisk Academy
    </div>
    <div class="strip-red" style="left:84px;top:0;width:7px;height:60px;"></div>
    <h2 class="headline" style="top:6px;right:auto;left:96px;font-size:26px;">Teaching</h2>
    <h3 class="headline" style="top:38px;right:auto;left:96px;font-size:13px;">Workplace Skills</h3>
    <ul class="ticks" style="left:232px;top:4px;font-size:11px;line-height:1.5;">
      <li>Covering Social Media.</li>
      <li>Texting &amp; Cell Phones.</li>
      <li>Grooming &amp; Hygiene.</li>
    </ul>
    <div class="cta cta-red" style="left:352px;top:8px;width:56px;height:44px;font-size:14px;line-height:1.15;white-space:normal;text-align:center;">Free Preview!</div>
    <div class="photo" role="img" aria-label="Photo of three young adults" style="left:412px;top:0;width:56px;height:60px;"></div>
  </section>

</div>
</body>
</html>
```